Lark and Fern: Prespective and Balence in People's Lives Needs a Buissness Card Design

Lark and Fern Community Center is an organization that seeks to bring balance into people's lives. Main services include: guided meditation, group brainstorming, and guided counseling. Lark and Fern combines Eastern practices, i.e. Buddhism, Hinduism, and Taoism, with Western practices: therapy, group brainstorming and healing. We would like a double sided card: 1) front vertical with image, 2) back horizontal with information. The main colors for the card are red, white, black. Different finishes would be nice--please no high gloss. Matte, pearlized, embossing--used tactfully and sparingly would be nice. The card should convey balance/harmony in a modern world.

```html
<!DOCTYPE html>
<html lang="en">
<head>
<meta charset="utf-8">
<title>Lark and Fern Community Center – Business Card</title>
<link href="https://fonts.googleapis.com/css2?family=Poppins:wght@300;400;600&display=swap" rel="stylesheet">
<style>
  :root {
    --stage: #b9b9b9;
    --red: #c8202a;
    --red-deep: #a8141d;
    --red-soft: #e89a9c;
    --black: #0a0a0a;
    --white: #ffffff;
    --ink: #222222;
  }
  * { margin: 0; padding: 0; box-sizing: border-box; }
  html, body { width: 1200px; height: 662px; overflow: hidden; }
  body {
    background: var(--stage);
    font-family: "Poppins", sans-serif;
    position: relative;
  }

  /* Front: vertical card */
  .card-front {
    position: absolute;
    left: 98px; top: 48px;
    width: 330px; height: 580px;
    display: flex;
    overflow: hidden;
  }
  .card-front .half-light { width: 165px; height: 100%; background: var(--white); }
  .card-front .half-dark { width: 165px; height: 100%; background: var(--black); }
  .card-front .emblem {
    position: absolute;
    left: 42px; top: 166px;
    width: 248px; height: 248px;
  }

  /* Back: horizontal card */
  .card-back {
    position: absolute;
    left: 443px; top: 297px;
    width: 578px; height: 331px;
    background: var(--white);
    overflow: hidden;
  }
  .band {
    position: absolute; left: 0; width: 100%; height: 10px;
    background: linear-gradient(to right, var(--black) 0 288px, var(--red) 288px 100%);
  }
  .band-top { top: 0; }
  .band-bottom { bottom: 0; height: 11px; }

  .figure-area {
    position: absolute;
    right: 0; top: 10px;
    width: 165px; height: 310px;
    background: linear-gradient(to right, var(--red-soft), var(--red) 45%, var(--red-deep));
    clip-path: polygon(62% 0, 100% 0, 100% 100%, 0 100%, 18% 78%, 42% 40%, 50% 22%);
  }

  .center-name {
    position: absolute;
    left: 25px; top: 30px;
    font-weight: 600;
    font-size: 28px;
    color: var(--red);
    white-space: nowrap;
  }
  .motto {
    position: absolute;
    left: 0; top: 78px; width: 524px;
    text-align: center;
    font-size: 14px;
    color: var(--ink);
  }
  .person-name {
    position: absolute;
    left: 25px; top: 136px;
    font-weight: 300;
    font-size: 31px;
    color: var(--red);
  }
  .person-role {
    position: absolute;
    left: 143px; top: 175px;
    font-weight: 300;
    font-size: 13px;
    color: var(--ink);
  }
  .contact {
    position: absolute;
    left: 25px; top: 216px;
    font-weight: 300;
    font-size: 13.5px;
    color: var(--ink);
    border-collapse: collapse;
  }
  .contact td { height: 22.7px; padding: 0; }
  .contact .label { width: 80px; }
</style>
</head>
<body>
  <section class="card-front" aria-label="Card front">
    <div class="half-light"></div>
    <div class="half-dark"></div>
    <svg class="emblem" viewBox="0 0 248 248" role="img" aria-label="Seated meditation figure silhouette in a red and white circle">
      <defs>
        <linearGradient id="emblem-fill" x1="0" x2="1">
          <stop offset="0" stop-color="#c8202a"/>
          <stop offset="0.5" stop-color="#7a1418"/>
          <stop offset="1" stop-color="#e0a0a2"/>
        </linearGradient>
      </defs>
      <circle cx="124" cy="124" r="124" fill="url(#emblem-fill)"/>
    </svg>
  </section>

  <section class="card-back" aria-label="Card back">
    <div class="band band-top"></div>
    <div class="figure-area" role="img" aria-label="Red silhouette of a seated meditating figure"></div>
    <h1 class="center-name">Lark and Fern Community Center</h1>
    <p class="motto">Your Motto here....</p>
    <h2 class="person-name">Mara Quill</h2>
    <p class="person-role">Trainer</p>
    <table class="contact">
      <tr><td class="label">Address</td><td>: your address</td></tr>
      <tr><td class="label">Phone</td><td>: 123 4567 890</td></tr>
      <tr><td class="label">Email</td><td>info@larkandfern.com</td></tr>
      <tr><td class="label">website</td><td>www.larkandfern.com</td></tr>
    </table>
    <div class="band band-bottom"></div>
  </section>
</body>
</html>
```